Medical Software Company needs Wordpress Website Template

Vontrix needs a gorgeous wordpress template (and about 10 subtemplates or custom pages with MINOR variations from the primary page - just one color difference in each) that will represent its modern, forward thinking approach to medical software development.

The structure of the final website will be one main entry page with icons leading to subsections of the site. Each subsection of the site will have a distinct look (minor variation from the main theme) to indicate to the site visitor which section they are in. The subsections will represent the different medical fields of the users of our software.

Materials to use:

You can download an image and our logo from the link below.
http://vontrixhq.net/marketing/vontrix_assets.zip

Themes we like:

We like the interactive social icons, the interactive slide show in the header, and the contact form in the footer of this theme:
http://pixelbazaar-demo.net/item/clinic-deluxe-site-theme/full_screen_preview/5810374

We like the openness (no boundaries around header image) and the navigation links (4 links to sub-sections) used in this theme:
http://www.layoutharbor-demo.net/demo/61742.html

We like the navigation links below the header
http://preview.qelvo-designs.net/index.php?bartype=desktop&theme=clinic

Target Market(s)

Doctors and other medical professionals.

Industry/Entity Type

Medical

Requirements
Must have
• + Interactive social media icons, contact form in page footer, customizable slideshow on the main page

```html
<!DOCTYPE html>
<html lang="en">
<head>
<meta charset="utf-8">
<title>Vontrix — Medical Software</title>
<link href="https://fonts.googleapis.com/css2?family=Open+Sans:wght@400;600;700;800&family=Oswald:wght@500;600&display=swap" rel="stylesheet">
<style>
:root{
  --page-bg:#dbeef8;
  --page-bg-2:#eef7fc;
  --nav:#3d4a57;
  --nav-dark:#2e3944;
  --nav-active:#1f8fd6;
  --brand:#1f7fc4;
  --red:#d9302c;
  --card-blue:#2a8fd4;
  --text:#444;
  --muted:#777;
  --footer:#2b2b2b;
  --footer-dark:#1d1d1d;
  --footer-text:#b9b9b9;
  --white:#fff;
}
*{box-sizing:border-box;margin:0;padding:0}
html,body{width:865px;height:1200px;overflow:hidden}
body{font-family:"Open Sans",Arial,sans-serif;color:var(--text);background:linear-gradient(180deg,var(--page-bg) 0,var(--page-bg-2) 460px,#fff 700px);font-size:9px;line-height:1.5}
.wrap{width:785px;margin:0 auto;position:relative}
.masthead{height:112px;position:relative}
.brand{position:absolute;left:0;top:30px;display:flex;align-items:center;gap:8px}
.brand-dot{width:26px;height:26px;border-radius:50%;background:var(--brand)}
.brand-name{font-size:32px;font-weight:700;color:var(--brand);letter-spacing:-.5px}
.social{position:absolute;right:0;top:26px;display:flex;gap:6px}
.social span{width:22px;height:22px;border-radius:3px;display:block}
.social .s1{background:#f07a22}.social .s2{background:#d9302c}.social .s3{background:#3b5b98}.social .s4{background:#f39a1d}
.search{position:absolute;right:0;top:58px;width:190px;height:22px;border:1px solid #b9cfdc;background:#fff;border-radius:2px;font-size:9px;color:#999;padding:4px 8px}
.main-nav{height:34px;background:linear-gradient(180deg,var(--nav),var(--nav-dark));display:flex}
.main-nav a{color:#fff;text-decoration:none;font-weight:700;font-size:11px;padding:0 20px;line-height:34px}
.main-nav a.active{background:var(--nav-active)}
.slider{margin-top:12px;height:270px;background:#fff;position:relative;display:flex}
.slide-text{width:300px;padding:60px 0 0 28px}
.slide-text h1{font-family:"Oswald",sans-serif;font-weight:600;font-size:30px;line-height:1.05;color:var(--red);text-transform:uppercase}
.slide-text h1 span{color:#333;font-size:22px;display:block}
.slide-text p{margin-top:10px;font-size:9px;color:var(--muted);width:210px}
.slide-photo{flex:1;background:linear-gradient(120deg,#e9f1f6,#c9dce8 55%,#9fc2da)}
.dots{position:absolute;left:28px;bottom:12px;display:flex;gap:5px}
.dots i{width:7px;height:7px;border-radius:50%;background:#ccc;display:block}
.dots i.on{background:var(--brand)}
.cards{display:flex;gap:6px;margin-top:14px}
.card{flex:1;height:232px;background:#fff;position:relative}
.card .pic{height:104px}
.card h3{font-size:15px;font-weight:600;text-align:center;margin-top:8px}
.card p{text-align:center;font-size:8px;padding:4px 16px;color:#fff}
.card .more{display:block;width:66px;margin:6px auto 0;background:var(--nav-dark);color:#fff;font-size:7px;font-weight:700;text-align:center;padding:4px 0}
.card.red{background:var(--red);color:#fff}
.card.blue{background:var(--card-blue);color:#fff}
.card.red .pic{background:linear-gradient(160deg,#f3f3f3,#d6dde2)}
.card.blue .pic{background:linear-gradient(160deg,#cfe6f5,#7fb6dc)}
.card.blue.b2 .pic{background:linear-gradient(160deg,#f4e8e0,#c9b4a8)}
.card.blue.b3 .pic{background:linear-gradient(160deg,#eaf3ea,#b6d0c8)}
.content{display:flex;gap:28px;margin-top:20px}
.welcome{flex:1}
.welcome h2{font-size:21px;font-weight:400;color:#333;margin-bottom:8px}
.welcome p{font-size:8px;color:var(--muted);margin-bottom:10px}
.why{width:215px}
.why h2{font-size:17px;font-weight:600;color:var(--red);margin-bottom:6px}
.why .pic{height:80px;background:linear-gradient(120deg,#e6eef4,#b9cfe0)}
.why h4{font-size:10px;margin-top:6px;color:#333}
.why p{font-size:8px;color:var(--muted)}
.site-footer{position:absolute;left:0;top:1000px;width:865px;height:200px;background:var(--footer);color:var(--footer-text)}
.foot-cols{display:flex;gap:30px;padding-top:14px}
.foot-cols h5{color:#fff;font-size:11px;font-weight:700;text-transform:uppercase;margin-bottom:8px}
.col{width:240px}
.field{display:flex;align-items:center;gap:6px;margin-bottom:5px;font-size:8px}
.field label{width:40px}
.field span{flex:1;height:14px;background:#3a3a3a;border:1px solid #4a4a4a}
.field.msg span{height:36px}
.submit{display:inline-block;background:#555;color:#fff;font-size:8px;padding:3px 10px;margin-left:46px}
.post{margin-bottom:8px;font-size:8px}
.post b{color:#fff;font-weight:600;display:block}
.info p{font-size:8px;margin-bottom:2px}
.foot-brand{display:flex;align-items:center;gap:6px;margin-top:10px;justify-content:flex-end}
.foot-brand i{width:16px;height:16px;border-radius:50%;background:var(--brand)}
.foot-brand span{font-size:20px;font-weight:700;color:#fff}
.copy{position:absolute;bottom:0;left:0;width:100%;height:22px;background:var(--footer-dark);font-size:8px;line-height:22px}
</style>
</head>
<body>
<div class="wrap">
  <header class="masthead">
    <div class="brand"><span class="brand-dot"></span><span class="brand-name">Vontrix</span></div>
    <div class="social" aria-label="Social links"><span class="s1"></span><span class="s2"></span><span class="s3"></span><span class="s4"></span></div>
    <div class="search">Search…</div>
  </header>
  <nav class="main-nav">
    <a class="active" href="#">Home</a><a href="#">About Us</a><a href="#">Products</a><a href="#">Services</a><a href="#">Contact Us</a><a href="#">Free Demo</a>
  </nav>
  <section class="slider">
    <div class="slide-text">
      <h1>We make your<span>practice our priority</span></h1>
      <p>Smart records, simple scheduling and secure billing built for busy clinics. Less paperwork, more time for patients.</p>
    </div>
    <div class="slide-photo" role="img" aria-label="Photo of smiling nurse and medical staff"></div>
    <div class="dots"><i class="on"></i><i></i><i></i></div>
  </section>
  <section class="cards">
    <article class="card red"><div class="pic" role="img" aria-label="Product image"></div><h3>Products Spotlight</h3><p>Explore our newest tools for charting, billing and patient follow up.</p><span class="more">LEARN MORE</span></article>
    <article class="card blue"><div class="pic" role="img" aria-label="Team photo"></div><h3>About Us</h3><p>A team of doctors and engineers building software for care.</p><span class="more">LEARN MORE</span></article>
    <article class="card blue b2"><div class="pic" role="img" aria-label="Doctor with patient photo"></div><h3>Services Provide</h3><p>Setup, training and support for practices of every size.</p><span class="more">LEARN MORE</span></article>
    <article class="card blue b3"><div class="pic" role="img" aria-label="Clinic photo"></div><h3>Meaningful Use</h3><p>Meet reporting rules with guided, certified workflows.</p><span class="more">LEARN MORE</span></article>
  </section>
  <section class="content">
    <div class="welcome">
      <h2>Welcome to Our Website Mainpage</h2>
      <p>Vontrix builds modern medical software for doctors and care teams. Our platform brings records, scheduling, prescriptions and billing together in one clean workspace, so your staff spends less time on screens and more time with patients. Every module is designed with clinicians and tested in real practices.</p>
      <p>Each specialty gets its own tailored view, from family medicine to cardiology and pediatrics. Choose the section that fits your field and see how our tools adapt to the way you already work.</p>
      <p>Our support team is available around the clock, with onboarding, data migration and training included. Join thousands of practices that trust us to keep their day running smoothly and their data safe.</p>
    </div>
    <aside class="why">
      <h2>Why Choose Us</h2>
      <div class="pic" role="img" aria-label="Photo of doctors consulting"></div>
      <h4>Care-first design</h4>
      <p>Fast, reliable tools shaped by clinicians, with secure cloud storage and friendly support.</p>
    </aside>
  </section>
</div>
<footer class="site-footer">
  <div class="wrap foot-cols">
    <div class="col">
      <h5>Contact Form</h5>
      <div class="field"><label>Name</label><span></span></div>
      <div class="field"><label>Email</label><span></span></div>
      <div class="field msg"><label>Message</label><span></span></div>
      <div class="field"><label>Code</label><span></span></div>
      <span class="submit">Submit</span>
    </div>
    <div class="col">
      <h5>Latest Blog Post</h5>
      <div class="post"><b>Blog title here</b>New charting updates make daily notes faster.</div>
      <div class="post"><b>Blog title here</b>Tips for a smooth switch to digital records.</div>
      <div class="post"><b>Blog title here</b>What the new reporting rules mean for you.</div>
    </div>
    <div class="col info">
      <h5>Contact Info</h5>
      <p>Vontrix Software</p>
      <p>Harbor Street 42, Suite 7</p>
      <p>Phone: 000-000-0000</p>
      <p>hello@vontrixhq.net</p>
      <div class="foot-brand"><i></i><span>Vontrix</span></div>
    </div>
  </div>
  <div class="copy"><div class="wrap">© 2013 Vontrix. All rights reserved. Terms of Use</div></div>
</footer>
</body>
</html>
```